依頼詳細
運動の嫌いな子でも気軽に身体を動かせるような教室を目指しています。
現在は低学年の女子が主な受講生なので、男子や高学年の子ども達にも興味を持っていただけたらありがたいです。
配布方法は新聞への折り込みなどを考えています。
白黒で印刷してもキレイに見えるデザインを希望します。
記載項目
現在使っているチラシ(wordファイル)を添付しています。
記載項目はその内容でお願いいたします。
サイズ
A4
ページ数
片面
希望イメージ
シンプル 複雑
単色 カラフル
暗い 明るい
日常 高級
遊び心 厳粛
未来的 伝統的
女性的 男性的
希望する色
納品ファイル
• 高解像度JPG (.jpg)
補足説明
■ 選んだ理由

ぱっと目を引く明るいデザインと、雰囲気が当教室とマッチしていることから決定いたしました。
PRポインとや、目線の流れもわかりやすく、白黒バージョンも見やすかったです。

■ 提案者全員のお礼・コメント

ご提案いただいた皆様
この度は沢山のご提案をいただき、まことにありがとうございました。
初めてのポルテミカの利用でしたが、素晴らしいご提案をたくさんいただけたことに感激しました。
ぜひこれからも依頼させていただきたいと思います。
よろしくお願いいたします。

```html
<!DOCTYPE html>
<html lang="ja">
<head>
<meta charset="UTF-8">
<title>ひだまりキッズダンス青葉教室 生徒募集</title>
<link href="https://fonts.googleapis.com/css2?family=M+PLUS+Rounded+1c:wght@500;800;900&family=Noto+Sans+JP:wght@400;700;900&display=swap" rel="stylesheet">
<style>
:root{
  --orange:#f39a1e;
  --orange-deep:#ea6d10;
  --orange-light:#fbd08a;
  --cream:#fff6e6;
  --pink:#e8336f;
  --blue:#1e6fbf;
  --navy:#1b4f95;
  --ink:#222;
  --white:#fff;
}
*{margin:0;padding:0;box-sizing:border-box}
html,body{width:837px;height:1200px;overflow:hidden;background:#fff}
.flyer{position:relative;width:837px;height:1200px;overflow:hidden;
  font-family:"Noto Sans JP",sans-serif;color:var(--ink);
  background:linear-gradient(180deg,var(--orange) 0%,var(--orange-light) 45%,var(--cream) 62%,#fff 78%)}
.rays{position:absolute;left:0;top:0;width:837px;height:760px;
  background:radial-gradient(circle at 60% 40%,rgba(255,255,255,.55) 0,rgba(255,255,255,0) 60%)}
.photo-main{position:absolute;right:0;top:150px;width:420px;height:470px;
  background:linear-gradient(180deg,#f4c79b 0%,#d89a6a 55%,#3b3b3b 100%);border-radius:40px 0 0 40px;opacity:.9}
.headline-top{position:absolute;top:18px;left:0;width:100%;height:90px}
.lead-left,.lead-right{position:absolute;top:14px;font:800 24px/1.25 "M PLUS Rounded 1c",sans-serif;color:var(--white);text-align:center;
  text-shadow:0 0 4px var(--orange-deep)}
.lead-left{left:30px}
.lead-right{right:30px}
.fun{position:absolute;left:0;right:0;top:4px;text-align:center;font:900 62px/1 "M PLUS Rounded 1c",sans-serif;color:var(--pink);
  -webkit-text-stroke:10px #fff;paint-order:stroke fill}
.catch{position:absolute;top:150px;left:0;right:0;text-align:center;font:900 72px/1 "M PLUS Rounded 1c",sans-serif;color:var(--blue);
  -webkit-text-stroke:12px #fff;paint-order:stroke fill;letter-spacing:-1px}
.schedule{position:absolute;left:40px;top:330px;font:900 42px/1 "M PLUS Rounded 1c",sans-serif;color:var(--white);text-shadow:0 0 6px var(--orange-deep)}
.schedule .day{display:inline-block;width:78px;height:78px;border-radius:50%;background:var(--white);color:var(--orange-deep);
  text-align:center;line-height:78px;font-size:56px;margin:0 8px;vertical-align:middle;text-shadow:none}
.time{position:absolute;left:40px;top:425px;font:900 48px/1 "M PLUS Rounded 1c",sans-serif;color:var(--white);text-shadow:0 0 6px var(--orange-deep)}
.price-box{position:absolute;left:40px;top:570px;width:300px;height:190px;background:var(--orange-deep);border-radius:18px;color:var(--white);text-align:center}
.price-box .label{font:900 40px/1 "M PLUS Rounded 1c",sans-serif;margin-top:20px}
.price-box .amount{font:900 110px/1 "M PLUS Rounded 1c",sans-serif;letter-spacing:-2px}
.price-box .amount small{font-size:48px}
.price-note{position:absolute;left:40px;top:770px;width:310px;font-size:14px;line-height:1.5;color:var(--orange-deep);font-weight:700}
.price-note .sub{color:#666;font-weight:400;font-size:12px}
.recruit{position:absolute;right:40px;top:695px;text-align:center;font:900 70px/1.1 "M PLUS Rounded 1c",sans-serif;color:var(--pink);
  -webkit-text-stroke:10px #fff;paint-order:stroke fill}
.recruit .first{font-size:52px;display:block;text-align:left}
.instructor{position:absolute;left:40px;top:850px;width:330px;display:flex;gap:12px;align-items:flex-start}
.instructor .portrait{width:82px;height:82px;border-radius:50%;background:linear-gradient(#e9b9b9,#c54a4a);flex:none}
.instructor p{font-size:14px;line-height:1.45;font-weight:700}
.instructor .name{font-size:17px}
.songs{position:absolute;right:40px;top:860px;font-size:19px;font-weight:900;color:var(--blue);text-align:right}
.notes{position:absolute;right:40px;top:900px;width:420px;font-size:13px;line-height:1.55;color:#333;list-style:none}
.notes li::before{content:"・"}
.footer{position:absolute;left:0;bottom:0;width:100%;height:125px;background:var(--navy);color:var(--white);padding:14px 30px}
.footer .school{font:800 30px/1.1 "M PLUS Rounded 1c",sans-serif}
.footer .place{font-size:17px;margin-top:10px}
.footer .tel{font-size:17px;margin-top:6px;font-weight:700}
</style>
</head>
<body>
<main class="flyer">
  <div class="rays"></div>
  <div class="photo-main" role="img" aria-label="笑顔でポーズをとるダンス教室の女の子の写真"></div>

  <header class="headline-top">
    <p class="lead-left">小学生も、<br>保育園児も</p>
    <h1 class="fun">楽しく踊って</h1>
    <p class="lead-right">体力に自信<br>のないお子様でも</p>
  </header>
  <h2 class="catch">体力もリズム感もアップ!</h2>

  <p class="schedule">毎週<span class="day">水</span>曜日</p>
  <p class="time">17:00～18:00</p>

  <section class="price-box">
    <p class="label">1レッスン</p>
    <p class="amount">500<small>円</small></p>
  </section>
  <p class="price-note">入会手続き無し。月に1回から、1回毎のお支払いで、お気軽にご参加ください!<br><span class="sub">※他の方法をご希望の方はご相談ください。</span></p>

  <p class="recruit"><span class="first">ただいま、</span>生徒募集中!</p>

  <section class="instructor">
    <div class="portrait" role="img" aria-label="講師の写真"></div>
    <p><span class="name">講師:川村 美和</span><br>元エアロビクスインストラクター<br>ダンス指導歴15年<br>リズム体操講師</p>
  </section>

  <p class="songs">人気アニメソング、J-POP、ダンスヒット</p>
  <ul class="notes">
    <li>動きやすい服装、上履き、飲み物をご持参ください。</li>
    <li>見学・体験はいつでも歓迎です。お気軽にどうぞ。</li>
    <li>教室はスポーツ保険に加入しています。</li>
    <li>レッスン中の保護者の見学も可能です。</li>
    <li>保護者の方は送迎のご協力をお願いします。</li>
  </ul>

  <footer class="footer">
    <p class="school">ひだまりキッズダンス青葉教室</p>
    <p class="place">青葉コミュニティセンター2階　研修室　毎週水曜日(17:00～18:00)</p>
    <p class="tel">TEL:080-1234-5678(森川 拓海)　TEL:080-8765-4321(森川 里奈)</p>
  </footer>
</main>
</body>
</html>
```